Letterhead

We are looking for a basic letterhead. It should include our logo, website - northbaykitchenware.com, phone 907.318.5926, toll free 855.419.2836, and fax 907.318.4150, along with our address 4378 Birchmont Avenue, Anchorage, AK 99612. I want something that will look good printed in color or black and white.

```html
<!DOCTYPE html>
<html lang="en">
<head>
<meta charset="utf-8">
<title>North Bay Kitchenware — Letterhead</title>
<link rel="stylesheet" href="https://fonts.googleapis.com/css2?family=Montserrat:wght@700&family=Source+Sans+3:wght@400&display=swap">
<style>
  :root {
    --canvas-bg: #ffffff;
    --sheet-bg: #ffffff;
    --sheet-edge: #3a3a3a;
    --brand-blue: #1d4486;
    --rule-grey: #6b6b6b;
    --contact-grey: #555555;
  }
  * { margin: 0; padding: 0; box-sizing: border-box; }
  html, body {
    width: 1200px;
    height: 851px;
    overflow: hidden;
    background: var(--canvas-bg);
  }
  .canvas {
    position: relative;
    width: 1200px;
    height: 851px;
  }
  .sheet {
    position: absolute;
    left: 204px;
    top: 1px;
    width: 597px;
    height: 843px;
    background: var(--sheet-bg);
    border: 1px solid var(--sheet-edge);
  }
  .brand-name {
    position: absolute;
    left: 68px;
    top: 82px;
    width: 216px;
    font-family: "Montserrat", sans-serif;
    font-weight: 700;
    color: var(--brand-blue);
    text-transform: uppercase;
    line-height: 1;
  }
  .brand-name__main {
    display: block;
    font-size: 38px;
    letter-spacing: 0.5px;
  }
  .brand-name__sub {
    display: block;
    margin-top: 6px;
    font-size: 17.5px;
    letter-spacing: 1.8px;
  }
  .divider {
    position: absolute;
    left: 294px;
    top: 39px;
    width: 5px;
    height: 111px;
    border-left: 1px solid var(--rule-grey);
    border-right: 1px solid var(--rule-grey);
  }
  .contact {
    position: absolute;
    left: 306px;
    top: 43px;
    list-style: none;
    font-family: "Source Sans 3", sans-serif;
    font-size: 8.6px;
    color: var(--contact-grey);
  }
  .contact__line {
    height: 18px;
    line-height: 14px;
  }
</style>
</head>
<body>
<div class="canvas">
  <section class="sheet">
    <h1 class="brand-name">
      <span class="brand-name__main">North Bay</span>
      <span class="brand-name__sub">Kitchenware</span>
    </h1>
    <div class="divider"></div>
    <ul class="contact">
      <li class="contact__line">4378 Birchmont Avenue,</li>
      <li class="contact__line">Anchorage, AK 99612.</li>
      <li class="contact__line">Toll free: 855.419.2836</li>
      <li class="contact__line">Tel: 907.318.5926</li>
      <li class="contact__line">Fax: 907.318.4150</li>
      <li class="contact__line">northbaykitchenware.com</li>
    </ul>
  </section>
</div>
</body>
</html>
```